Brisk Meadow Builders needs a product brochure

We need a new flyer for our Patio Perch Lounge. Here is some of the copy your will need.
"Turn your back yard into the ultimate entertianment venue with the stunning Patio Perch Lounge!"
"Entertain family & friends in your very own back yard!"
"Available with or without solar and comes in a variety of colors"
"The Patio Perch Lounge measures 5' deep by 10' wide and is 9'-6" at it's highest point"
"Constructed with treated 4x4's, primed then painted with Thornby Calder best exterior paint for years of care free enjoyment. Also, Marlow Pendt Keystead shingles are dimensional, have a 25 year warranty and are rated for 150 mph winds!"
"TV Mount included. Shelves and TV are sold separately"
There also needs to be a box where we can add the price into later. The price can change from time to time due to material cost fluctuation.
Look and feel
Each slider illustrates characteristics of the customer's brand and the style your logo design should communicate.

```html
<!DOCTYPE html>
<html lang="en">
<head>
<meta charset="utf-8">
<title>Patio Perch Lounge Flyer – Brisk Meadow Builders</title>
<link rel="stylesheet" href="https://fonts.googleapis.com/css2?family=Oswald:wght@500;700&family=Open+Sans:wght@400;600;700&display=swap">
<style>
:root{
  --green:#4c9a35;
  --green-dark:#3a7d28;
  --orange:#f6a623;
  --orange-deep:#ee8f14;
  --ink:#333333;
  --paper:#ffffff;
  --canvas:#eef0ee;
  --photo-warm-a:#8a6b4e;
  --photo-warm-b:#3e4a3a;
  --photo-sky-a:#c9d6dc;
  --photo-sky-b:#5c6f4a;
}
*{margin:0;padding:0;box-sizing:border-box}
html,body{width:795px;height:1200px;overflow:hidden;background:var(--canvas)}
body{position:relative;font-family:"Open Sans",Arial,sans-serif;color:var(--ink)}
.page{position:absolute;left:19px;width:757px;background:var(--paper);overflow:hidden;box-shadow:0 2px 8px rgba(0,0,0,.18)}
.page-front{top:14px;height:534px}
.page-back{top:574px;height:612px}
.art{position:absolute;inset:0}
.abs{position:absolute}
.head{font-family:"Oswald",Impact,sans-serif;font-weight:700;text-transform:uppercase;line-height:1}
.brand{font-family:"Oswald",Impact,sans-serif;font-weight:700;color:var(--green);display:flex;align-items:center;gap:7px;text-transform:uppercase;letter-spacing:.5px}
.brand .dot{width:14px;height:14px;border-radius:50%;background:var(--orange);flex:none}

/* front */
.front-brand{left:520px;top:46px;font-size:17px;line-height:1.05;width:200px}
.front-brand-left{left:40px;top:420px;font-size:16px;line-height:1.05;width:200px}
.contact{left:40px;top:470px;font-size:13px;font-weight:700;color:var(--green);display:flex;align-items:center;gap:6px}
.contact-web{left:40px;top:494px;font-size:10px;color:var(--ink)}
.price-box{left:226px;top:368px;width:76px;height:30px;background:var(--orange);color:#fff;text-align:center;font-family:"Oswald",Impact,sans-serif;font-weight:700;line-height:1}
.price-box small{display:block;font-size:8px;padding-top:4px}
.price-box span{font-size:13px}
.tag-line-1{right:40px;top:410px;font-size:17px;color:#fff}
.tag-line-2{right:30px;top:432px;padding:4px 12px;background:var(--orange);font-size:22px;color:#fff}
.tag-line-3{right:36px;top:466px;font-size:48px;color:#fff}

/* back */
.hero-copy{left:22px;top:28px;width:300px;color:#fff;text-align:center}
.hero-copy .l1{font-size:25px}
.hero-copy .l2{font-size:40px;color:var(--orange);margin-top:4px}
.hero-copy .l3{font-size:40px;margin-top:2px}
.hero-copy .l4{font-size:19px;margin-top:6px}
.avail{left:340px;top:300px;width:417px;background:var(--orange);color:#fff;padding:7px 16px;font-size:15px;text-align:center}
.measure-pill{left:378px;top:352px;width:340px;background:var(--green);color:#fff;border-radius:14px;text-align:center;font-size:10px;font-weight:700;padding:3px 10px}
.measure-pill em{display:block;font-style:normal;font-weight:600;font-size:9.5px}
.body-copy{left:368px;top:398px;width:360px;font-size:9.5px;line-height:1.45;text-align:center}
.tv-note{left:368px;top:470px;width:360px;font-size:9.5px;font-weight:700;color:var(--orange-deep);text-align:center}
.back-brand{left:500px;top:520px;font-size:16px;line-height:1.05;width:150px}
.back-web{left:500px;top:582px;font-size:10px;font-weight:600;color:var(--green)}
</style>
</head>
<body>

<section class="page page-front" aria-label="Flyer front">
  <svg class="art" viewBox="0 0 757 534" width="757" height="534">
    <defs>
      <linearGradient id="photoWarm" x1="0" y1="0" x2="1" y2="1">
        <stop offset="0" stop-color="var(--photo-warm-a)"/>
        <stop offset="1" stop-color="var(--photo-warm-b)"/>
      </linearGradient>
      <linearGradient id="photoSky" x1="0" y1="0" x2="0" y2="1">
        <stop offset="0" stop-color="var(--photo-sky-a)"/>
        <stop offset="1" stop-color="var(--photo-sky-b)"/>
      </linearGradient>
    </defs>
    <!-- orange swoosh -->
    <path d="M250,0 H420 C400,170 300,320 0,420 V330 C180,260 250,140 250,0 Z" fill="var(--orange)"/>
    <!-- green edge band -->
    <path d="M210,0 H262 C258,150 180,270 0,330 V300 C160,240 215,130 210,0 Z" fill="var(--green)"/>
    <!-- customer photo -->
    <path d="M0,0 H210 C215,130 160,240 0,300 Z" fill="url(#photoWarm)" role="img" aria-label="Photo of a man serving drinks at the outdoor bar"/>
    <!-- product photo -->
    <rect x="330" y="90" width="410" height="300" fill="url(#photoSky)" role="img" aria-label="Photo of the Patio Perch Lounge bar shelter in a back yard with stools and plants"/>
    <!-- sun decoration -->
    <circle cx="590" cy="26" r="16" fill="var(--orange)" role="img" aria-label="Sun illustration"/>
    <!-- price inset photo -->
    <rect x="226" y="298" width="76" height="70" fill="url(#photoWarm)" stroke="#fff" stroke-width="3" role="img" aria-label="Close-up photo of bar shelves with bottles"/>
    <!-- bottom green band -->
    <path d="M300,534 C360,450 420,410 520,400 H757 V534 Z" fill="var(--green)"/>
    <!-- phone icon -->
    <g transform="translate(40,470)">
      <circle cx="7" cy="7" r="7" fill="var(--green)"/>
      <path d="M4.5,3.5 l1.6,0 l.7,2 l-1,.8 a5,5 0 0 0 2.4,2.4 l.8,-1 l2,.7 v1.6 a1,1 0 0 1 -1,1 A7,7 0 0 1 3.5,4.5 a1,1 0 0 1 1,-1 z" fill="#fff"/>
    </g>
  </svg>

  <div class="abs brand front-brand"><span class="dot"></span><span>Brisk Meadow<br>Builders</span></div>
  <div class="abs brand front-brand-left"><span class="dot"></span><span>Brisk Meadow<br>Builders</span></div>
  <div class="abs contact"><span style="width:14px"></span>555-014-2290</div>
  <div class="abs contact-web">www.briskmeadowbuilders.com</div>

  <div class="abs price-box"><small>PRICE</small><span>$0000</span></div>

  <div class="abs head tag-line-1">Entertain family &amp; friends</div>
  <div class="abs head tag-line-2">In your very own</div>
  <div class="abs head tag-line-3">Back yard!</div>
</section>

<section class="page page-back" aria-label="Flyer back">
  <svg class="art" viewBox="0 0 757 612" width="757" height="612">
    <defs>
      <linearGradient id="photoWarmB" x1="0" y1="0" x2="1" y2="1">
        <stop offset="0" stop-color="var(--photo-warm-a)"/>
        <stop offset="1" stop-color="var(--photo-warm-b)"/>
      </linearGradient>
      <linearGradient id="photoSkyB" x1="0" y1="0" x2="0" y2="1">
        <stop offset="0" stop-color="var(--photo-sky-a)"/>
        <stop offset="1" stop-color="var(--photo-sky-b)"/>
      </linearGradient>
    </defs>
    <rect x="0" y="0" width="340" height="250" fill="var(--green)"/>
    <rect x="0" y="250" width="340" height="362" fill="url(#photoWarmB)" role="img" aria-label="Photo of wooden wall shelf holding wine bottles and hanging glasses"/>
    <rect x="180" y="400" width="120" height="70" fill="var(--photo-warm-a)" stroke="#fff" stroke-width="3" role="img" aria-label="Inset photo of a wooden drink holder"/>
    <rect x="340" y="0" width="417" height="300" fill="url(#photoSkyB)" role="img" aria-label="Photo of two people relaxing at the Patio Perch Lounge bar"/>
    <rect x="660" y="515" width="80" height="60" fill="url(#photoSkyB)" stroke="#fff" stroke-width="3" role="img" aria-label="Small photo of the bar shelter"/>
  </svg>

  <div class="abs head hero-copy">
    <div class="l1">Turn your back yard into</div>
    <div class="l2">The ultimate</div>
    <div class="l3">Entertainment</div>
    <div class="l4">Venue with the stunning<br>Patio Perch Lounge!</div>
  </div>

  <div class="abs head avail">Available with or without solar and comes in a variety of colors</div>
  <div class="abs measure-pill">The Patio Perch Lounge measures<em>5' deep by 10' wide and is 9'-6" at it's highest point</em></div>
  <p class="abs body-copy">Constructed with treated 4x4's, primed then painted with Thornby Calder best exterior paint for years of care free enjoyment. Also, Marlow Pendt Keystead shingles are dimensional, have a 25 year warranty and are rated for 150 mph winds!</p>
  <p class="abs tv-note">TV Mount included. Shelves and TV are sold separately</p>

  <div class="abs brand back-brand"><span class="dot"></span><span>Brisk Meadow<br>Builders</span></div>
  <div class="abs back-web">www.briskmeadow.com</div>
</section>

</body>
</html>
```